Catholic composer needs poster for new musical, "THE STONE AND THE VIGIL, the Harvest Musical"

We need a dynamic poster for "The Stone and the Vigil," a new musical written for Catholic dinner theater. We need you to create an iconic design like you see in posters for classic musicals, like "Rosa Calendula," Lantern of the Harbour," or "Gilded." In our musical, “fire” represents the Holy Spirit, who showers man with his merciful love.

Miraculous events occur. A mighty wind from heaven fills the house. Tongues of fire appear over their heads. They speak in other tongues that are understandable by all present. They are emboldened to go out and tell the Good News to the world, despite the risks associated with evangelizing this fledgling religion. They exclaim, “Lord, you will show us the path to life.”

Target Market(s)

The audience is adult members of Catholic churches. But don't make the design look too "churchy."

Requirements
Must have
• Photoshop or Illustrated file with layers, or vector format.
Should not have
• Really don't want photos.

```html
<!DOCTYPE html>
<html lang="en">
<head>
<meta charset="utf-8">
<title>The Stone and the Vigil – The Harvest Musical</title>
<link rel="stylesheet" href="https://fonts.googleapis.com/css2?family=Cinzel:wght@400;700&family=Montserrat:wght@400;600;700&family=Shadows+Into+Light&display=swap">
<style>
  :root {
    --red-deep: #4a0508;
    --red-mid: #9a1014;
    --red-glow: #c8221b;
    --gold: #f4d41c;
    --flame-core: #ffd36a;
    --flame-mid: #f07a1a;
    --hands: #2a0a0a;
    --white: #ffffff;
  }
  * { margin: 0; padding: 0; box-sizing: border-box; }
  html, body { width: 863px; height: 1200px; overflow: hidden; background: var(--red-deep); }
  .poster {
    position: relative;
    width: 863px;
    height: 1200px;
    overflow: hidden;
    background:
      radial-gradient(ellipse 70% 55% at 50% 48%, var(--red-glow) 0%, var(--red-mid) 45%, var(--red-deep) 100%);
    color: var(--white);
  }
  .title {
    position: absolute;
    left: 58px;
    top: 58px;
    font-family: "Cinzel", serif;
    color: var(--gold);
    line-height: 0.9;
  }
  .title-line { display: flex; align-items: center; }
  .title-small {
    display: flex;
    flex-direction: column;
    font-size: 48px;
    line-height: 0.95;
    margin-right: 10px;
    text-align: center;
  }
  .title-big { font-size: 150px; font-weight: 400; letter-spacing: 2px; }
  .title-line.second { margin-left: 70px; margin-top: -6px; }
  .subtitle {
    position: absolute;
    left: 560px;
    top: 330px;
    font-family: "Montserrat", sans-serif;
    font-weight: 700;
    font-size: 16px;
    letter-spacing: 1px;
    color: var(--gold);
  }
  .artwork {
    position: absolute;
    left: 90px;
    top: 390px;
    width: 683px;
    height: 400px;
    border-radius: 50%;
    background: radial-gradient(ellipse 35% 55% at 50% 42%, var(--flame-core) 0%, var(--flame-mid) 40%, rgba(154,16,20,0.0) 75%),
                radial-gradient(ellipse 55% 18% at 50% 88%, var(--hands) 0%, rgba(42,10,10,0) 100%);
  }
  .credits {
    position: absolute;
    left: 0;
    width: 100%;
    top: 940px;
    text-align: center;
    font-family: "Montserrat", sans-serif;
  }
  .credits-line { font-size: 12px; font-weight: 600; letter-spacing: 1px; }
  .author { font-size: 30px; font-weight: 700; letter-spacing: 1px; margin-top: 2px; }
  .quote {
    position: absolute;
    left: 210px;
    top: 1020px;
    font-family: "Shadows Into Light", cursive;
    font-size: 34px;
    line-height: 1.15;
    letter-spacing: 2px;
  }
  .quote .second { display: block; margin-left: 30px; }
  .details {
    position: absolute;
    left: 40px;
    top: 1096px;
    font-family: "Montserrat", sans-serif;
    font-size: 10px;
    line-height: 1.5;
    opacity: 0.9;
  }
  .website {
    position: absolute;
    right: 40px;
    bottom: 36px;
    font-family: "Montserrat", sans-serif;
    font-size: 12px;
    font-weight: 600;
    letter-spacing: 1px;
  }
</style>
</head>
<body>
  <main class="poster">
    <h1 class="title">
      <span class="title-line">
        <span class="title-small"><span>THE</span></span>
        <span class="title-big">STONE</span>
      </span>
      <span class="title-line second">
        <span class="title-small"><span>&amp;</span><span>THE</span></span>
        <span class="title-big">VIGIL</span>
      </span>
    </h1>
    <p class="subtitle">THE HARVEST MUSICAL</p>

    <div class="artwork" role="img" aria-label="Illustration of a glowing flame rising above two open, upturned hands"></div>

    <div class="credits">
      <p class="credits-line">A NEW MUSICAL FOR CATHOLIC DINNER THEATER BY</p>
      <p class="author">MILES HARWOOD</p>
    </div>

    <p class="quote">“O SPIRIT COME,<span class="second">YOU ARE MERCIFUL LOVE”</span></p>

    <ul class="details" style="list-style:none">
      <li>Music</li>
      <li>Book</li>
      <li>Cast</li>
      <li>Tickets</li>
    </ul>

    <p class="website">WWW.THESTONEANDTHEVIGIL.COM</p>
  </main>
</body>
</html>
```